Newly opened kids play space needs brochure to show what our space has to offer

Tri-fold color brochure with same aethetic as website (www.fernhollowplayhouse.com) that provides a comprehensive and visual overview of what our play space is comprised of. Features of the brochure should include our logo, "A Garrick and Pellinger-inspired Play Space in the Poconos", photos of: Dedicated Infant Play Area; Cafe and Free WiFi; Weekly Themed Activities; Unique Classes; Parties and Events. Photos also of our open play area with children playing within it. Info within the brochure should include our location, hours. Please take some copy from : https://www.facebook.com/fernhollowtinkerplayhouse/?ref=bookmarks
and from the Plan Your Visit part of the website. I have a lot of photos to use; is there a way to put in generic photo placeholders and I can pick which photos of mine to go into the various areas of the brochure, or if you need the photos ahead of time, please let me know the best way to proceed. I am attaching the logo files for now.

Font styles to use
Sans Serif

Colors
85cae6
cee9f5
86cfc6
cfeae6
fdf9cf
fff3d1
eaf2ce
cadf82

Requirements
Must have
• Eye catching placement of photos; color scheme similar to website and logo colors
Should not have
• Brochure should be simple, not too colorful - no primary colors, not too crowded.

```html
<!DOCTYPE html>
<html lang="en">
<head>
<meta charset="utf-8">
<title>Fern Hollow Play Space – Brochure Inside Spread</title>
<link rel="stylesheet" href="https://fonts.googleapis.com/css2?family=Source+Sans+3:ital,wght@0,400;0,600;1,400;1,800&display=swap">
<style>
  :root {
    --stage: #ecebe6;
    --page: #fbf9f0;
    --story-bg: #fdf9cf;
    --ink: #3d3a36;
    --heading: #5b2b1f;
    --sky: #85cae6;
    --teal: #86cfc6;
    --lime: #cadf82;
    --mint: #cfeae6;
    --coral: #f08a6a;
    --lilac: #b08ad0;
    --leaf: #7cc46a;
  }
  * { box-sizing: border-box; margin: 0; padding: 0; }
  html, body { width: 1200px; height: 917px; overflow: hidden; }
  body { background: var(--stage); font-family: "Source Sans 3", sans-serif; color: var(--ink); position: relative; }

  .panel { position: absolute; background: var(--page); box-shadow: 0 2px 6px rgba(0,0,0,.12); overflow: hidden; }
  .spread { left: 53px; top: 50px; width: 704px; height: 816px; }
  .features { left: 799px; top: 50px; width: 349px; height: 816px; }

  .story-field { position: absolute; left: 357px; top: 0; width: 347px; height: 816px; background: var(--story-bg); }
  .soft-circle { position: absolute; border-radius: 50%; background: var(--mint); opacity: .45; }

  .photo { position: absolute; }

  .tagline-tile {
    position: absolute; left: 9px; top: 23px; width: 172px; height: 150px; border-radius: 8px;
    background: linear-gradient(135deg, #2f8fc0 0%, #3fa7a9 50%, #a8cf5a 100%);
    display: flex; flex-direction: column; justify-content: center; align-items: center;
    font-style: italic; font-weight: 800; color: #fff; font-size: 38px; line-height: 36px; letter-spacing: 1px;
  }

  .story { position: absolute; left: 381px; top: 40px; width: 300px; }
  .story h2 { text-align: center; font-weight: 600; font-size: 28px; line-height: 34px; color: var(--heading); margin-bottom: 2px; }
  .story .rule { display: block; margin: 0 auto 14px; }
  .story p { font-size: 14.4px; line-height: 19.8px; letter-spacing: .15px; text-align: justify; margin-bottom: 16px; }

  .welcome-quote { position: absolute; left: 354px; top: 533px; font-style: italic; font-size: 16.5px; line-height: 20px; color: #222; white-space: nowrap; }

  .divider { position: absolute; left: 0; top: 577px; height: 8px; width: 580px; background: linear-gradient(90deg, #2f8fc0, #58b9a8, #a8cf5a); }
  .swatches { position: absolute; left: 584px; top: 577px; display: flex; gap: 2px; }
  .swatches span { width: 10px; height: 8px; display: block; }

  .feature { position: absolute; left: 0; top: 0; width: 349px; }
  .feature h3 { position: absolute; left: 1px; font-weight: 400; font-size: 15px; color: var(--heading); padding-left: 7px; border-left: 3px solid var(--c); line-height: 16px; white-space: nowrap; }
  .feature p { position: absolute; left: 9px; width: 169px; font-size: 12.2px; line-height: 18.4px; text-align: justify; }
  .feature .photo { left: 188px; width: 144px; border-bottom: 4px solid var(--c); }
</style>
</head>
<body>

<section class="panel spread">
  <div class="story-field"></div>
  <div class="soft-circle" style="left:530px;top:290px;width:300px;height:300px;"></div>

  <div class="tagline-tile"><span>PLAY</span><span>LEARN</span><span>GROW</span></div>

  <div class="photo" role="img" aria-label="Children and parents sitting in a circle on a braided rug" style="left:185px;top:23px;width:169px;height:150px;background:linear-gradient(160deg,#7a6fb0,#c77a8a 60%,#d9a56c);"></div>
  <div class="photo" role="img" aria-label="Flowers, wooden figures and stars on a play table" style="left:9px;top:177px;width:172px;height:391px;background:linear-gradient(180deg,#3e8db8 0%,#c8869a 30%,#3f8bb0 55%,#8b5a4a 80%,#b07a5a);"></div>
  <div class="photo" role="img" aria-label="Children crafting around a table" style="left:185px;top:177px;width:169px;height:151px;background:linear-gradient(150deg,#7fb0c8,#b98a6a 55%,#7a5b49);"></div>
  <div class="photo" role="img" aria-label="Girl sitting among tree roots in the woods" style="left:185px;top:332px;width:169px;height:236px;background:linear-gradient(170deg,#7e6a52,#a8865e 50%,#c7a58a);"></div>

  <article class="story">
    <h2>Our Story</h2>
    <svg class="rule" width="150" height="10" viewBox="0 0 150 10"><line x1="0" y1="5" x2="68" y2="5" stroke="#c8c2a4"/><circle cx="75" cy="5" r="3" fill="none" stroke="#b9b39a"/><line x1="82" y1="5" x2="150" y2="5" stroke="#c8c2a4"/></svg>
    <p>Fern Hollow was born out of a desire for a different kind of play space in the Poconos. A play space that celebrates the quieter, natural curiosities of the child.</p>
    <p>In our rushed daily lives filled with noise, electronics, and running on overdrive, Fern Hollow is a place that brings us down a notch and let’s us simply, play.</p>
    <p>Combining Garrick and Pellinger philosophies in the materials and activities we have thoughtfully selected to introduce at Fern Hollow, our play space provides an open-ended, multi-sensory approach to play, nourishing the whole child. We have a range of classes for all ages, and are happy to host your next party or event as well.</p>
    <p>Catch up on work with our free Wi-Fi or simply relax in our cafe while having a Crema Pod, tea, simple healthy snacks or a cold beverage.</p>
  </article>
  <p class="welcome-quote">“We look forward to welcoming you to Fern Hollow”</p>

  <div class="divider"></div>
  <div class="swatches">
    <span style="background:#6b5a4e"></span><span style="background:#4a90d0"></span><span style="background:#9c7ac8"></span><span style="background:#e06a8a"></span><span style="background:#e9e04a"></span><span style="background:#9a9a3a"></span><span style="background:#7cc46a"></span><span style="background:#e96a3a"></span><span style="background:#f0a070"></span>
  </div>

  <div class="photo" role="img" aria-label="Children playing in the open play area with wooden toys" style="left:0;top:588px;width:691px;height:208px;background:linear-gradient(180deg,#c9b8a2 0%,#b58a7a 50%,#2c3f78 100%);"></div>
</section>

<section class="panel features">
  <div class="soft-circle" style="left:-60px;top:280px;width:250px;height:430px;"></div>

  <div class="feature" style="--c:var(--sky)">
    <h3 style="top:52px">Dedicated Infant Play Area</h3>
    <p style="top:79px">Bond safely with your baby while being within eyeshot of the main play area.</p>
    <div class="photo" role="img" aria-label="Parent with a baby in the infant play area" style="top:21px;height:148px;background:linear-gradient(160deg,#c9b39a,#7c6b8c 60%,#2a2a3a);"></div>
  </div>

  <div class="feature" style="--c:var(--leaf)">
    <h3 style="top:212px">Cafe and Free WiFi</h3>
    <p style="top:235px">Take a break or catch up on work while enjoying Crema Pod coffee, beverages, and snacks.</p>
    <div class="photo" role="img" aria-label="Parent enjoying a coffee in the cafe lounge" style="top:177px;height:148px;background:linear-gradient(160deg,#9aa4a8,#5a4f52 55%,#a57a5a);"></div>
  </div>

  <div class="feature" style="--c:var(--coral)">
    <h3 style="top:366px">Weekly Themed Activities</h3>
    <p style="top:392px">Stories, crafts, and activities change weekly to celebrate the seasons and the world around us.</p>
    <div class="photo" role="img" aria-label="Children doing a themed craft at a table" style="top:333px;height:148px;background:linear-gradient(160deg,#b8c0c8,#c9a870 55%,#d8b04a);"></div>
  </div>

  <div class="feature" style="--c:var(--lilac)">
    <h3 style="top:525px">Unique Classes</h3>
    <p style="top:548px">Our multi-age, multi-sensory approach to traditional classes nurtures the whole child in a creative and fun way.</p>
    <div class="photo" role="img" aria-label="Children dancing and moving during a class" style="top:490px;height:148px;background:linear-gradient(160deg,#c98a5a,#8aa0a0 50%,#7a6a7a);"></div>
  </div>

  <div class="feature" style="--c:var(--teal)">
    <h3 style="top:680px">Parties and Events</h3>
    <p style="top:705px">Forget a stress, have a fun and enjoy with kids in delightfully conducted events and parties.</p>
    <div class="photo" role="img" aria-label="Kids playing games at a party" style="top:646px;height:148px;background:linear-gradient(160deg,#c9c4c0,#8a7aa0 50%,#4aa0a8);"></div>
  </div>
</section>

</body>
</html>
```